Build Distinctive Business Card: Public Relations Government Relations firm

I have logo and colors done (attached) need a very cool way to present it on a business card (can be two sided if need be).

Public Relations Government Relations firm

Info:

Mark Tillson, CEO
Keystone Public Relations
2786 West Harlow Blvd.
Los Angeles CA 90047
(o) 213.555.0148
(f) 213.555.0193
mark@keystonekpr-example.com

Target Market(s)

Government relations, public relations, lobbyist, I was a past State Senator

Industry/Entity Type

Business

Contact Information for Business Card

Info:

Mark Tillson, CEO
Keystone Public Relations
2786 West Harlow Blvd.
Los Angeles CA 90047
(o) 213.555.0148
(f) 213.555.0193
mark@keystonekpr-example.com
@marktillson

Requirements
Must have
• A sense of balance given logo is already done.
• It's a government relations firm really.
• Lobbyist type.
• Senatorial type...

```html
<!DOCTYPE html>
<html lang="en">
<head>
<meta charset="utf-8">
<title>Keystone Public Relations – Business Card</title>
<link rel="stylesheet" href="https://fonts.googleapis.com/css2?family=Cinzel:wght@400;600&family=PT+Sans:wght@400;700&display=swap">
<style>
  :root {
    --page: #ffffff;
    --card-dark: #0c0c0c;
    --card-mid: #1d1d1d;
    --brand-blue: #1a8fd0;
    --brand-blue-deep: #0e5f98;
    --ink-light: #f2f2f2;
    --ink-soft: #b9c3cc;
  }
  html, body {
    margin: 0;
    width: 1200px;
    height: 809px;
    overflow: hidden;
    background: var(--page);
  }
  .canvas {
    position: relative;
    width: 1200px;
    height: 809px;
  }
  .card {
    position: absolute;
    background: linear-gradient(160deg, var(--card-mid) 0%, var(--card-dark) 55%, #151515 100%);
    box-shadow: 0 10px 28px rgba(0,0,0,0.28);
    overflow: hidden;
  }
  .card--front {
    left: 70px;
    top: 250px;
    width: 580px;
    height: 330px;
  }
  .card--back {
    left: 760px;
    top: 150px;
    width: 340px;
    height: 510px;
  }
  .corner-frame {
    position: absolute;
    left: 0;
    top: 0;
  }
  .holder {
    position: absolute;
    left: 62px;
    top: 40px;
    font-family: "Cinzel", serif;
    color: var(--ink-light);
    font-size: 17px;
    letter-spacing: 2.5px;
    line-height: 1.5;
  }
  .holder__role {
    display: block;
    padding-left: 48px;
  }
  .brand {
    position: absolute;
    display: flex;
    align-items: center;
    gap: 12px;
  }
  .card--front .brand {
    left: 158px;
    top: 118px;
  }
  .brand__disc {
    flex: none;
    border-radius: 50%;
    border: 5px solid var(--brand-blue);
    box-sizing: border-box;
  }
  .card--front .brand__disc {
    width: 84px;
    height: 84px;
  }
  .brand__text {
    display: flex;
    flex-direction: column;
    font-family: "PT Sans", sans-serif;
    color: var(--brand-blue);
  }
  .brand__name {
    font-weight: 700;
    font-size: 44px;
    line-height: 1;
  }
  .brand__tagline {
    font-size: 10.5px;
    letter-spacing: 2.2px;
    text-transform: uppercase;
    color: var(--brand-blue-deep);
    margin-top: 4px;
    padding-left: 4px;
  }
  .contact {
    position: absolute;
    right: 34px;
    top: 200px;
    margin: 0;
    font-family: "Cinzel", serif;
    font-style: normal;
    font-size: 12.5px;
    letter-spacing: 2px;
    line-height: 1.45;
    color: var(--ink-light);
    text-align: right;
  }
  .contact span { display: block; }
  .card--back .brand {
    left: 50%;
    top: 50%;
    transform: translate(-50%, -50%);
    flex-direction: column;
    gap: 18px;
  }
  .card--back .brand__disc {
    width: 170px;
    height: 170px;
    border-width: 8px;
  }
  .card--back .brand__name {
    font-size: 40px;
  }
</style>
</head>
<body>
<main class="canvas">
  <section class="card card--front" aria-label="Business card front">
    <svg class="corner-frame" width="580" height="330" viewBox="0 0 580 330" aria-hidden="true">
      <path d="M0 0 H215 V6 H6 V120 H0 Z" fill="var(--brand-blue)"/>
      <path d="M580 330 H395 V324 H574 V200 H580 Z" fill="var(--brand-blue)"/>
    </svg>

    <div class="holder">
      <span class="holder__name">Mark Tillson</span>
      <span class="holder__role">CEO</span>
    </div>

    <div class="brand">
      <span class="brand__disc" aria-hidden="true"></span>
      <span class="brand__text">
        <span class="brand__name">Keystone</span>
        <span class="brand__tagline">Public Relations</span>
      </span>
    </div>

    <address class="contact">
      <span>West Harlow Blvd 2786</span>
      <span>Los Angeles CA 90047</span>
      <span>213.555.0148</span>
      <span>213.555.0193</span>
      <span>mark@keystonekpr-example.com</span>
    </address>
  </section>

  <section class="card card--back" aria-label="Business card back">
    <div class="brand">
      <span class="brand__disc" aria-hidden="true"></span>
      <span class="brand__text">
        <span class="brand__name">Keystone</span>
      </span>
    </div>
  </section>
</main>
</body>
</html>
```